GLINT -- book design (5 x 8) boy 14 caught up in the 1838 Lower Canadian rebellion against the Brits

Boy must sell the book. So attractive while historic. Below is a well known picture drawn at the time of what the rebels looked like. My boy would probably have more in common with the guy in white than the others -- he was a lawyer's son.
TITLE: GLINT
AUTHOR: DOROTHEA KINSELLA

```html
<!DOCTYPE html>
<html lang="en">
<head>
<meta charset="utf-8">
<title>Glint — Dorothea Kinsella</title>
<link rel="stylesheet" href="https://fonts.googleapis.com/css2?family=Playfair+Display:wght@400;700&display=swap">
<style>
  :root {
    --backdrop: #e7e5e2;
    --cover-black: #0b0b0c;
    --photo-dark: #18191c;
    --photo-mid: #55575b;
    --photo-light: #c4c4c6;
    --piece-blue: #33466a;
    --piece-blue-deep: #1e2a40;
    --title-red: #b81d27;
    --frame-red: #a01c24;
    --author-white: #f6f6f6;
  }
  * { box-sizing: border-box; margin: 0; padding: 0; }
  html, body {
    width: 1200px;
    height: 789px;
    overflow: hidden;
    background: var(--backdrop);
  }
  .canvas {
    width: 1200px;
    height: 789px;
    display: flex;
    align-items: center;
    justify-content: center;
  }
  .book-cover {
    position: relative;
    width: 450px;
    height: 720px;
    background: var(--cover-black);
    overflow: hidden;
    box-shadow: 0 10px 30px rgba(0, 0, 0, 0.25);
  }
  .cover-photo {
    position: absolute;
    inset: 0;
    background:
      radial-gradient(ellipse 17% 40% at 50% 50%, var(--piece-blue) 0%, var(--piece-blue-deep) 55%, rgba(30, 42, 64, 0) 100%),
      radial-gradient(ellipse 14% 30% at 80% 30%, rgba(20, 20, 22, 0.85) 0%, rgba(20, 20, 22, 0) 100%),
      radial-gradient(ellipse 16% 22% at 22% 86%, rgba(20, 20, 22, 0.8) 0%, rgba(20, 20, 22, 0) 100%),
      linear-gradient(90deg, var(--cover-black) 0%, var(--photo-dark) 25%, var(--photo-mid) 60%, var(--photo-light) 100%);
  }
  .cover-frame {
    position: absolute;
    inset: 28px;
    border: 1px solid var(--frame-red);
    pointer-events: none;
  }
  .cover-title {
    position: absolute;
    top: 262px;
    left: 0;
    right: 0;
    text-align: center;
    font-family: "Playfair Display", Georgia, serif;
    font-weight: 700;
    font-size: 92px;
    line-height: 1;
    color: var(--title-red);
  }
  .cover-author {
    position: absolute;
    right: 48px;
    bottom: 50px;
    font-family: "Playfair Display", Georgia, serif;
    font-weight: 400;
    font-size: 26px;
    line-height: 1;
    color: var(--author-white);
  }
</style>
</head>
<body>
  <main class="canvas">
    <article class="book-cover">
      <div class="cover-photo" role="img" aria-label="Black and white close-up photograph of carved chess pieces on a board, the central standing piece tinted steel blue"></div>
      <div class="cover-frame"></div>
      <h1 class="cover-title">Glint</h1>
      <p class="cover-author">Dorothea Kinsella</p>
    </article>
  </main>
</body>
</html>
```